Bakery Business Cards

We are in need of business cards for our bakery business--something non-generic that reflects our business and will stand out. We are a wholesale bakery that primarily services in-store bakeries, casinos, schools, distributors, and fund-raising companies. The family business was founded in 1960. (www.marlowsovenworks.com)

```html
<!DOCTYPE html>
<html lang="en">
<head>
<meta charset="utf-8">
<title>Marlow's Ovenworks — Business Card</title>
<link href="https://fonts.googleapis.com/css2?family=Montserrat:wght@400;600;700&display=swap" rel="stylesheet">
<style>
  :root {
    --page-bg: #d2d3d5;
    --brand-blue: #2d4fa0;
    --ink-blue: #2b4fa8;
    --ink-dark: #333333;
    --accent-red: #b5222a;
    --card-white: #ffffff;
    --sketch-grey: #ececee;
  }
  * { box-sizing: border-box; margin: 0; padding: 0; }
  html, body { width: 1200px; height: 1000px; overflow: hidden; }
  body {
    background: var(--page-bg);
    font-family: "Montserrat", Arial, sans-serif;
    position: relative;
  }
  .card {
    position: absolute;
    left: 303px;
    width: 588px;
    height: 380px;
    overflow: hidden;
  }
  .card--front { top: 88px; background: var(--brand-blue); }
  .card--back { top: 526px; height: 381px; background: var(--card-white); }

  .pastry-pattern {
    position: absolute; inset: 0;
    background:
      radial-gradient(circle at 8% 18%, rgba(80,70,160,0.35) 0 14%, transparent 15%),
      radial-gradient(circle at 92% 12%, rgba(80,70,160,0.3) 0 16%, transparent 17%),
      radial-gradient(circle at 6% 85%, rgba(80,70,160,0.3) 0 18%, transparent 19%),
      radial-gradient(circle at 94% 80%, rgba(80,70,160,0.3) 0 16%, transparent 17%);
  }
  .sketch-pattern {
    position: absolute; inset: 0;
    background:
      radial-gradient(circle at 5% 50%, var(--sketch-grey) 0 22%, transparent 23%),
      radial-gradient(circle at 97% 75%, var(--sketch-grey) 0 20%, transparent 21%),
      radial-gradient(circle at 75% 100%, #f3f3f4 0 14%, transparent 15%),
      radial-gradient(circle at 70% 5%, #f3f3f4 0 12%, transparent 13%);
  }

  .front-name {
    position: absolute;
    left: 0; right: 0; top: 128px;
    text-align: center;
    color: var(--card-white);
    font-weight: 700;
    font-size: 42px;
    line-height: 1.15;
  }

  .back-name {
    position: absolute;
    left: 25px; top: 26px;
    color: var(--ink-blue);
    font-weight: 700;
    font-size: 17px;
    line-height: 1.2;
  }
  .address {
    position: absolute;
    right: 25px;
    text-align: right;
    color: var(--ink-blue);
    font-size: 17px;
    line-height: 24px;
  }
  .address--street { top: 23px; }
  .address--mail { bottom: 23px; }

  .tagline {
    position: absolute;
    left: 195px; top: 131px;
    font-weight: 700;
    font-size: 27px;
    line-height: 39px;
    color: var(--ink-dark);
    letter-spacing: 0.5px;
  }
  .tagline .accent { color: var(--accent-red); }

  .contact {
    position: absolute;
    left: 23px; bottom: 22px;
    list-style: none;
    color: var(--ink-blue);
    font-size: 17px;
    line-height: 28px;
  }
  .contact li { display: flex; align-items: center; gap: 12px; }
  .contact svg { width: 18px; height: 18px; fill: var(--ink-dark); }
</style>
</head>
<body>
  <section class="card card--front">
    <div class="pastry-pattern" role="img" aria-label="Faint pattern of line-drawn pies and pastries"></div>
    <h1 class="front-name">Marlow's<br>Ovenworks</h1>
  </section>

  <section class="card card--back">
    <div class="sketch-pattern" role="img" aria-label="Light grey sketches of pies, apples, wheat and pastries"></div>
    <p class="back-name">Marlow's<br>Ovenworks</p>
    <address class="address address--street">
      Marlow's Ovenworks, Inc.<br>1175 Millstone Ave<br>Fairview City, OK 73000
    </address>
    <p class="tagline">SERVING<br><span class="accent">SWEETNESS</span><br>SINCE <span class="accent">1960</span></p>
    <ul class="contact">
      <li>
        <svg viewBox="0 0 24 24" aria-hidden="true"><path d="M6.6 10.8a15.1 15.1 0 0 0 6.6 6.6l2.2-2.2a1 1 0 0 1 1-.25 11.4 11.4 0 0 0 3.6.57 1 1 0 0 1 1 1V20a1 1 0 0 1-1 1A17 17 0 0 1 3 4a1 1 0 0 1 1-1h3.5a1 1 0 0 1 1 1c0 1.25.2 2.45.57 3.57a1 1 0 0 1-.25 1z"/></svg>
        555.014.2290
      </li>
      <li>
        <svg viewBox="0 0 24 24" aria-hidden="true"><path d="M20 4H4a2 2 0 0 0-2 2v12a2 2 0 0 0 2 2h16a2 2 0 0 0 2-2V6a2 2 0 0 0-2-2zm0 4-8 5-8-5V6l8 5 8-5z"/></svg>
        contact@marlowsovenworks.com
      </li>
    </ul>
    <address class="address address--mail">
      Mailing address:<br>P.O Box 402117<br>Cedar Point, OK 73000
    </address>
  </section>
</body>
</html>
```